Website redesign www.brindlecovepc.com law firm site

Need to redesign the website that I currently have to look more modern and professional. Would also like to be able to make updates and post without having a huge hassle. See current www.brindlecovepc.com. I just think that it looks very immature and it's very templated there's no ability for me to make posts or Add links or anything like that

Target Market(s)

California people looking for a powerhouse attorney in

Industry/Entity Type

Legal

Number of Pages Required

3 page

Font styles to use
Serif
Sans Serif

Colors
ec1f27
000000
ffffff

Requirements
Must have
• Must be mobile friendly. Must look professional and have ability to post links to other websites. Must have ability to post blogs or articles. Would like to be able to read my Quindral account and also have the ability to upload forms for people to download
Nice to have
• Simple design easy to use and not cluttered with too much text

```html
<!DOCTYPE html>
<html lang="en">
<head>
<meta charset="utf-8">
<title>Brindle Cove P.C. — California Law Firm</title>
<link href="https://fonts.googleapis.com/css2?family=Cinzel:wght@400;700&family=Lato:ital,wght@0,400;0,700;1,400&display=swap" rel="stylesheet">
<style>
:root{
  --red:#ec1f27;
  --black:#000000;
  --white:#ffffff;
  --ink:#222222;
  --text:#333333;
  --muted:#8a8a8a;
  --card-gray:#58585a;
  --panel:#f3f3f3;
  --line:#e2e2e2;
  --footer:#23262e;
  --footer-line:#3a3e48;
  --serif:'Cinzel', Georgia, serif;
  --sans:'Lato', Arial, sans-serif;
}
*{box-sizing:border-box;margin:0;padding:0}
html,body{width:1200px;height:3377px;overflow:hidden;background:var(--white);font-family:var(--sans);color:var(--text)}
.page{position:relative;width:1200px;height:3377px}
.abs{position:absolute}

/* header */
.brand{left:120px;top:14px;color:var(--red);font-family:var(--serif);font-size:38px;line-height:42px;text-align:center}
.brand small{display:block;font-size:18px;line-height:24px}
.call{left:800px;top:30px;display:flex;align-items:center;gap:10px}
.call .lbl{font-size:13px;color:var(--muted);line-height:16px}
.call .num{font-size:20px;color:var(--red);line-height:22px}
.social-top{left:1005px;top:38px;display:flex;gap:8px;font-size:11px;color:var(--muted)}

/* nav */
.nav{left:0;top:104px;width:1200px;height:44px;background:var(--red)}
.nav ul{position:absolute;left:99px;width:1002px;height:44px;display:flex;list-style:none}
.nav li{flex:1;display:flex;align-items:center;justify-content:center;color:var(--white);font-family:var(--serif);font-size:14px;border-left:1px solid rgba(255,255,255,.35)}
.nav li:first-child{flex:0 0 68px;background:#111;border-left:0}

/* hero */
.hero-photo{left:99px;top:148px;width:684px;height:425px;background:linear-gradient(120deg,#2b2c30 0%,#5d5650 45%,#b49a7c 75%,#e7dccd 100%)}
.hero-title{left:128px;top:245px;width:560px;color:var(--white);font-size:34px;line-height:44px}
.hero-sub{left:128px;top:347px;color:var(--white);font-size:13px;display:flex;align-items:center;gap:10px}
.hero-sub i{width:13px;height:13px;border-radius:50%;border:3px solid var(--white);background:#999}
.btn{display:inline-flex;align-items:center;justify-content:center;font-family:var(--serif);font-size:14px}
.btn-red{background:var(--red);color:var(--white)}
.btn-line{border:1px solid var(--red);color:var(--ink);background:var(--white)}
.hero-btn{left:128px;top:391px;width:197px;height:36px}
.badges{left:99px;top:573px;width:684px;height:90px;background:#e6e6e6}
.badge-a{left:200px;top:555px;width:92px;height:92px;border-radius:50%;background:var(--white);border:5px solid #2a4f8f}
.badge-b{left:350px;top:557px;width:86px;height:86px;border-radius:50%;background:#f5f5f5;border:3px solid #777}
.badge-c{left:495px;top:590px;width:200px;height:36px;background:#8d9aa8;border-radius:3px}

.consult{left:783px;top:148px;width:318px;height:515px;background:var(--panel)}
.consult-head{height:77px;background:#2a2a2a;color:var(--white);font-family:var(--serif);font-size:23px;display:flex;align-items:center;justify-content:center;position:relative}
.consult-head:after{content:"";position:absolute;left:150px;bottom:-12px;border:12px solid transparent;border-bottom:0;border-top-color:#2a2a2a}
.field{position:absolute;left:22px;width:277px;height:44px;background:var(--white);border:1px solid #ddd;font-size:12px;color:#444;padding:12px 10px}
.consult .send{position:absolute;left:22px;top:427px;width:277px;height:44px}

/* about */
.kicker{width:64px;height:2px;background:var(--red)}
.h2{font-family:var(--serif);font-size:36px;color:var(--ink);text-align:center;letter-spacing:1px}
.h2 em{font-style:normal;color:var(--red)}
.about-title{left:99px;top:708px;width:650px}
.about-title .kicker{margin:0 auto 8px 170px}
.about-text{left:118px;top:781px;width:614px;text-align:center;font-size:13.5px;line-height:26px;color:#222}
.about-btns{left:290px;top:960px;display:flex;gap:10px}
.about-btns .btn{width:128px;height:36px}
.video-frame{left:757px;top:718px;width:345px;height:278px;background:var(--red)}
.video{left:767px;top:712px;width:337px;height:273px;background:linear-gradient(160deg,#3a64a8 0%,#6b8cc2 40%,#8a7d6a 75%,#4a4036 100%)}
.play{left:900px;top:814px}

/* practice */
.practice{left:99px;top:1048px;width:1002px;height:514px;background:linear-gradient(180deg,#ece9e6,#f6f4f2 60%,#ebe8e5)}
.practice-title{left:99px;top:1065px;width:1002px}
.practice-title .kicker{margin:0 auto 8px}
.card{top:1210px;width:323px;height:250px;background:var(--card-gray);clip-path:polygon(0 0,96% 0,100% 8%,96% 16%,96% 100%,0 100%)}
.card h3{margin-top:60px;text-align:center;color:var(--white);font-family:var(--serif);font-weight:400;font-size:21px}
.card p{margin:15px 22px 0 18px;text-align:center;color:var(--white);font-size:13px;line-height:22px}
.card .more{position:absolute;left:0;bottom:0;width:96%;height:33px;background:var(--red);color:var(--white);font-size:13px;display:flex;align-items:center;justify-content:center}
.icon-circle{top:1160px;width:90px;height:90px;border-radius:50%;background:var(--card-gray);display:flex;align-items:flex-start;justify-content:center;padding-top:22px}
.view-all{left:535px;top:1497px;width:130px;height:34px;border:2px solid #333;background:var(--white);color:#222}

/* reviews */
.reviews-title{left:99px;top:1612px;width:1002px}
.reviews-title .kicker{margin:0 auto 8px}
.review{top:1775px;width:320px;height:250px;background:#f5f5f5;border:1px solid var(--line);text-align:center}
.review h4{margin-top:88px;font-family:var(--serif);font-weight:400;font-size:16px;color:#222;letter-spacing:1px}
.review p{margin:20px 40px 0;font-style:italic;font-size:14px;line-height:22px;color:#222}
.review p b{color:#222;font-size:18px}
.avatar{top:1710px;width:114px;height:114px;border-radius:50%;border:6px solid var(--white);box-shadow:0 0 0 1px var(--line);background:linear-gradient(180deg,#c9ced4,#8d949c)}
.dots{left:576px;top:2058px;display:flex;gap:5px}
.dots i{width:13px;height:13px;border-radius:50%;background:#8d9185}
.dots i.on{background:var(--red)}
.divider{left:99px;top:2125px;width:1002px;height:2px;background:#ddd}

/* blog */
.blog-title{left:99px;top:2178px;width:1002px}
.blog-title .kicker{margin:0 auto 8px}
.post{top:2272px;width:320px;height:495px;background:#f5f5f5;border:1px solid var(--line);text-align:center}
.post .photo{height:258px}
.post h4{margin-top:20px;font-family:var(--serif);font-weight:400;font-size:15.5px;color:#222;letter-spacing:.5px}
.post .date{margin-top:30px;color:var(--red);font-size:13px;display:flex;justify-content:center;align-items:center;gap:8px}
.post p{margin:12px 28px 0;font-size:13px;line-height:20px;color:#222}
.post .read{margin-top:14px;font-family:var(--serif);font-size:13px;color:var(--red)}

/* footer */
.footer{left:0;top:2817px;width:1200px;height:560px;background:var(--footer);color:#9aa0aa}
.f-h{font-family:var(--serif);font-size:17px;color:var(--white);letter-spacing:1px}
.f-links{font-size:12.5px;line-height:32px;color:#8a909b}
.f-vline{left:627px;top:2883px;width:1px;height:160px;background:var(--footer-line)}
.f-hline{left:99px;top:3089px;width:1002px;height:1px;background:var(--footer-line)}
.f-social{display:flex;align-items:center;gap:24px}
.f-bottom{left:0;top:3123px;width:1200px;text-align:center;font-size:12.5px;color:#8a909b}
.f-bottom b{color:var(--white);font-weight:400}
.f-bottom span{margin:0 20px}
.f-brand{left:0;top:3175px;width:1200px;text-align:center;color:var(--white);font-family:var(--serif);font-size:40px;line-height:44px}
.f-brand small{display:block;font-size:18px;line-height:22px}
.f-note{left:99px;top:3278px;width:1002px;text-align:center;font-size:12.5px;line-height:22px;color:#7e848f}
</style>
</head>
<body>
<div class="page">

  <!-- Header -->
  <div class="abs brand">Brindle Cove<small>P.C</small></div>
  <div class="abs call">
    <svg width="24" height="24" viewBox="0 0 24 24"><path d="M6.6 10.8a15 15 0 0 0 6.6 6.6l2.2-2.2a1 1 0 0 1 1-.25 11 11 0 0 0 3.6.6 1 1 0 0 1 1 1V20a1 1 0 0 1-1 1A17 17 0 0 1 3 4a1 1 0 0 1 1-1h3.5a1 1 0 0 1 1 1 11 11 0 0 0 .6 3.6 1 1 0 0 1-.25 1z" fill="#9a9a9a"/></svg>
    <div><div class="lbl">Call Us</div><div class="num">123-456-7890</div></div>
  </div>
  <div class="abs social-top"><span>Facetome</span><span>Linkwell</span><span>Avero</span></div>

  <nav class="abs nav">
    <ul>
      <li>Home</li><li>Attorney Profile</li><li>Practice Areas</li><li>Client Reviews</li><li>Links</li><li>Contact Us</li>
    </ul>
  </nav>

  <!-- Hero -->
  <div class="abs hero-photo" role="img" aria-label="Photo of a lawyer signing documents at a desk"></div>
  <h1 class="abs hero-title" style="font-weight:400">Solutions To The Most Challenging Problems</h1>
  <div class="abs hero-sub"><i></i>We will provide you with clear guidance and answers to your problems</div>
  <div class="abs btn btn-red hero-btn">Free Consultation</div>
  <div class="abs badges"></div>
  <div class="abs badge-a"></div>
  <div class="abs badge-b"></div>
  <div class="abs badge-c"></div>

  <aside class="abs consult">
    <div class="consult-head">Free consultation!</div>
    <div class="field" style="top:143px">Name :</div>
    <div class="field" style="top:198px">Email :</div>
    <div class="field" style="top:253px">Phone :</div>
    <div class="field" style="top:308px;height:104px">Message</div>
    <div class="btn btn-red send">Submit</div>
  </aside>

  <!-- About -->
  <div class="abs about-title"><div class="kicker"></div><h2 class="h2" style="font-weight:400">About <em>Brindle Cove P.C</em></h2></div>
  <p class="abs about-text">Brindle Cove P.C. is owned by Maren T. Ashby, a dedicated and caring professional who uses her broad range of skills as a California lawyer to bring consumers and business owners exceptionally strong legal representation that achieves best results. She works with people from across the northern region of California, from the Northern border to the Central Valley region. They bring her legal concerns and problems that occur in many areas of law, including Real Estate, Family law, Business Law, Bankruptcy, Criminal Law and Civil Litigation.</p>
  <div class="abs about-btns"><div class="btn btn-red">Submit</div><div class="btn btn-line">Download</div></div>
  <div class="abs video-frame"></div>
  <div class="abs video" role="img" aria-label="Video still of a Lady Justice statue against a blue sky"></div>
  <svg class="abs play" width="70" height="70" viewBox="0 0 70 70"><circle cx="35" cy="35" r="32" fill="rgba(0,0,0,.25)" stroke="#fff" stroke-width="3"/><path d="M28 22 L50 35 L28 48 Z" fill="#fff"/></svg>

  <!-- Practice Areas -->
  <div class="abs practice" role="img" aria-label="Faded background photo of law books on shelves"></div>
  <div class="abs practice-title"><div class="kicker"></div><h2 class="h2" style="font-weight:400">Practice <em>Areas</em></h2></div>

  <div class="abs icon-circle" style="left:215px"><svg width="36" height="30" viewBox="0 0 36 30"><rect x="2" y="7" width="32" height="21" rx="2" fill="none" stroke="#fff" stroke-width="2.5"/><path d="M12 7V3h12v4M2 15h32" stroke="#fff" stroke-width="2.5" fill="none"/></svg></div>
  <div class="abs icon-circle" style="left:553px"><svg width="34" height="32" viewBox="0 0 34 32"><path d="M3 16 L17 3 L31 16 M7 13v16h20V13" fill="none" stroke="#fff" stroke-width="2.5"/><rect x="14" y="19" width="6" height="10" fill="#fff"/></svg></div>
  <div class="abs icon-circle" style="left:892px"><svg width="24" height="34" viewBox="0 0 24 34"><circle cx="12" cy="5" r="4" fill="#fff"/><path d="M5 11h14v11h-3v11h-8V22H5z" fill="#fff"/></svg></div>

  <div class="abs card" style="left:99px"><h3>Business Law</h3><p>Small and medium-sized businesses have many of the same legal issues that affect large businesses, such as business structure, contracts, dispute resolution and litigation. At Brindle Cove</p><div class="more">Read More</div></div>
  <div class="abs card" style="left:437px"><h3>Real Estate Law</h3><p>At Brindle Cove P.C., we help Californians who need legal advice and representation for Real Estate Law activities, such as closings, contracts, title searches and more.</p><div class="more">Read More</div></div>
  <div class="abs card" style="left:776px;clip-path:none;width:325px"><h3>Bankruptcy</h3><p>If your finances are dwindling to the point where you can no longer pay your bills, and you are getting harassed by collection agents, it is time to visit Brindle Cove P.C.,</p><div class="more" style="width:100%">Read More</div></div>
  <div class="abs btn view-all">View All</div>

  <!-- Client Reviews -->
  <div class="abs reviews-title"><div class="kicker"></div><h2 class="h2" style="font-weight:400">Client <em>Reviews</em></h2></div>
  <div class="abs review" style="left:99px"><h4>Jarws Barrymre</h4><p><b>“</b> At vero eos et accusamus et iusto odio dignissimos ducimus qui blanditiis praesentium voluptatum deleniti atque corrupti quos <b>”</b></p></div>
  <div class="abs review" style="left:440px"><h4>Jarws Barrymre</h4><p><b>“</b> At vero eos et accusamus et iusto odio dignissimos ducimus qui blanditiis praesentium voluptatum deleniti atque corrupti quos <b>”</b></p></div>
  <div class="abs review" style="left:781px"><h4>Jarws Barrymre</h4><p><b>“</b> At vero eos et accusamus et iusto odio dignissimos ducimus qui blanditiis praesentium voluptatum deleniti atque corrupti quos <b>”</b></p></div>
  <div class="abs avatar" style="left:202px" role="img" aria-label="Client portrait"></div>
  <div class="abs avatar" style="left:543px" role="img" aria-label="Client portrait"></div>
  <div class="abs avatar" style="left:884px" role="img" aria-label="Client portrait"></div>
  <div class="abs dots"><i></i><i class="on"></i><i></i></div>
  <div class="abs divider"></div>

  <!-- Latest Blog -->
  <div class="abs blog-title"><div class="kicker"></div><h2 class="h2" style="font-weight:400">Latest <em>Blog</em></h2></div>
  <article class="abs post" style="left:99px">
    <div class="photo" role="img" aria-label="Photo of a scales of justice statue at sunset" style="background:linear-gradient(160deg,#6a7a92,#c9a36a 55%,#2a2620)"></div>
    <h4>Lorem ipsum dolor sit amet,</h4>
    <div class="date"><svg width="13" height="13" viewBox="0 0 13 13"><rect x="1" y="2" width="11" height="10" fill="none" stroke="#ec1f27" stroke-width="1.5"/><path d="M1 5h11" stroke="#ec1f27" stroke-width="1.5"/></svg>26 July, 2016</div>
    <p>Sed ut perspiciatis unde omnis iste natus error sit voluptatem accusantium doloremque laudantium, totam rem aperiam, eaque ipsa</p>
    <div class="read">Read More »</div>
  </article>
  <article class="abs post" style="left:440px">
    <div class="photo" role="img" aria-label="Photo of a business team meeting around a table" style="background:linear-gradient(160deg,#e8e8e8,#9ea3a9 50%,#2d2f33)"></div>
    <h4>Lorem ipsum dolor sit amet,</h4>
    <div class="date"><svg width="13" height="13" viewBox="0 0 13 13"><rect x="1" y="2" width="11" height="10" fill="none" stroke="#ec1f27" stroke-width="1.5"/><path d="M1 5h11" stroke="#ec1f27" stroke-width="1.5"/></svg>26 July, 2016</div>
    <p>Sed ut perspiciatis unde omnis iste natus error sit voluptatem accusantium doloremque laudantium, totam rem aperiam, eaque ipsa</p>
    <div class="read">Read More »</div>
  </article>
  <article class="abs post" style="left:781px">
    <div class="photo" role="img" aria-label="Photo of two lawyers standing in a law library" style="background:linear-gradient(160deg,#5a3a28,#8a6a4a 45%,#2a2420)"></div>
    <h4>Lorem ipsum dolor sit amet,</h4>
    <div class="date"><svg width="13" height="13" viewBox="0 0 13 13"><rect x="1" y="2" width="11" height="10" fill="none" stroke="#ec1f27" stroke-width="1.5"/><path d="M1 5h11" stroke="#ec1f27" stroke-width="1.5"/></svg>26 July, 2016</div>
    <p>Sed ut perspiciatis unde omnis iste natus error sit voluptatem accusantium doloremque laudantium, totam rem aperiam, eaque ipsa</p>
    <div class="read">Read More »</div>
  </article>

  <!-- Footer -->
  <footer class="abs footer"></footer>
  <div class="abs f-h" style="left:99px;top:2868px">Navigation</div>
  <div class="abs f-links" style="left:99px;top:2930px">Home<br>Attorney Profile<br>Practice Areas</div>
  <div class="abs f-links" style="left:353px;top:2930px">Client Reviews<br>Links<br>Contact Us</div>
  <div class="abs f-vline"></div>
  <div class="abs f-h" style="left:810px;top:2868px">Get Social</div>
  <div class="abs f-links" style="left:810px;top:2930px">
    <div class="f-social"><span style="width:12px;height:12px;background:#8a909b;border-radius:50%"></span>Facetome</div>
    <div class="f-social"><span style="width:12px;height:12px;background:#8a909b;border-radius:50%"></span>Linkwell</div>
    <div class="f-social"><span style="width:12px;height:12px;background:#8a909b;border-radius:50%"></span>Avero</div>
  </div>
  <div class="abs f-hline"></div>
  <div class="abs f-bottom">© 2016 <b>Brindle Cove, P.C.</b><span>|</span>Disclaimer<span>|</span>Site Map<span>|</span>Sign In</div>
  <div class="abs f-brand">Brindle Cove<small>P.C</small></div>
  <p class="abs f-note">When we say "FREE TO THE CONSUMER" we mean exactly that while we don't work for free, consumers will not be charged any attorney's fees. we seek to recover our attorney's fees from the manufacture and/or dealer pursuant to state and Federal laws.</p>

</div>
</body>
</html>
```